Divorce Lawyer Direct Mail Comparison Card

2 sided mailer to fit in 5.5 X 8.5 inch envelope. direct mail for divorce and family law firm practicing primarily at the Jersey Shore, New Jersey, USA. Comparison chart on one side and text explanation on the other side.
The card will be used in our envelope with our direct mail pieces

The reader will receive 2 to 3 envelopes and this piece will be included in all 3 mailing envelopes
Add a border and enough style to keep the card in the reader's hand and get them to flip both sides. We will utilize a textured stock. Your mission is to make the chart pop.
The zip file contains the chart for side one, the descriptive text for side 2 and the header and footer for side 1.
We are growing our firm fast and this mailed card will be a huge enhancement to our existing marketing. Thank you so much for participating!

Target Market(s)

people getting divorced or in family court

Industry/Entity Type

Legal

Font styles to use
Serif

Colors

Designer to choose colors to be used in the design.

Requirements
Must have
• easy to read
• color that eases the reader's transition
• make the reader flip the card and review both sides
• some style
• 2 sides
• address and phone at the bottom
Nice to have
• emphasize phone number and website
• emphasize Level 3 - our most popular option
Should not have
• no too many extra words

```html
<!DOCTYPE html>
<html lang="en">
<head>
<meta charset="utf-8">
<title>Bayview Family Law Group – Service Options Card</title>
<link href="https://fonts.googleapis.com/css2?family=Cormorant+Garamond:ital,wght@0,500;0,600;1,500&family=Montserrat:wght@300;400;600&display=swap" rel="stylesheet">
<style>
:root{
  --page:#e6e7e9;
  --card:#ffffff;
  --blue:#1f6fae;
  --blue-deep:#1a5d94;
  --blue-soft:#6a9fcb;
  --blue-pale:#9cbfdc;
  --gray:#dcdde0;
  --gray-light:#ececee;
  --ink:#2b2f36;
  --muted:#8a8e95;
  --white:#ffffff;
}
*{box-sizing:border-box;margin:0;padding:0}
html,body{width:1200px;height:960px;overflow:hidden}
body{background:var(--page);font-family:'Montserrat',Arial,sans-serif;color:var(--ink);position:relative}
.card{position:absolute;left:250px;width:700px;height:453px;background:var(--card);padding:14px;box-shadow:0 2px 8px rgba(0,0,0,.12)}
.card--front{top:17px}
.card--back{top:490px}

/* front */
.front-inner{position:relative;width:100%;height:100%;overflow:hidden;background:var(--card)}
.hero{position:absolute;left:0;top:0;width:672px;height:210px}
.hero-title{position:absolute;left:24px;top:18px;font-family:'Cormorant Garamond',Georgia,serif;color:var(--white)}
.hero-title .firm{display:inline-block;background:rgba(106,159,203,.75);padding:4px 14px;font-size:26px;font-style:italic;font-weight:500}
.hero-title .tagline{display:block;margin:4px 0 0 40px;background:rgba(106,159,203,.75);padding:3px 14px;font-size:17px;font-style:italic;width:max-content}
.levels{position:absolute;left:0;bottom:0;width:672px;display:flex;gap:5px;align-items:flex-end}
.level{flex:1;height:240px;background:var(--gray);padding:18px 14px;font-size:9.5px;line-height:1.45;color:var(--muted)}
.level:nth-child(2){background:var(--gray-light)}
.level .num{color:var(--blue);font-size:11px;font-weight:600;display:block;margin-bottom:6px}
.level h2{font-size:12.5px;font-weight:600;color:var(--ink);margin-bottom:10px}
.level--featured{height:270px;background:var(--blue);color:var(--white)}
.level--featured .num,.level--featured h2{color:var(--white)}
.level--featured h2{font-size:13.5px}
.level--featured p{font-size:10.5px}
.level--last{background:#d4d5d8;color:#55595f}

/* back */
.back-inner{width:100%;height:100%;display:flex;flex-direction:column;gap:6px}
.chart-title{height:44px;background:linear-gradient(90deg,var(--blue-soft),var(--blue-deep));color:var(--white);font-family:'Cormorant Garamond',Georgia,serif;font-weight:600;font-size:22px;letter-spacing:6px;display:flex;align-items:center;justify-content:center}
.chart{flex:1;display:grid;grid-template-columns:140px repeat(5,1fr);grid-template-rows:repeat(5,1fr);gap:4px;font-size:10.5px;text-align:center}
.chart div{display:flex;align-items:center;justify-content:center;background:var(--gray-light);color:#5a5e65;padding:0 4px}
.chart .col-head{background:var(--blue);color:var(--white);font-weight:600}
.chart .row-head{background:var(--white);color:#4a4e55;font-family:'Cormorant Garamond',Georgia,serif;font-size:13px;font-weight:600;line-height:1.1}
.chart .corner{background:var(--blue);color:var(--white);font-family:'Cormorant Garamond',Georgia,serif;font-size:14px}
.chart .row-feature{background:var(--blue-pale);color:var(--white);font-weight:600}
.chart .row-head.row-feature{background:var(--blue-soft);color:var(--white)}
.chart-footer{height:58px;background:var(--blue);color:var(--white);display:flex;align-items:center;padding:0 18px;font-size:10.5px;line-height:1.4}
.chart-footer .address{width:190px}
.chart-footer .divider{width:1px;height:32px;background:rgba(255,255,255,.5);margin:0 18px}
.chart-footer .contact strong{font-size:14px;font-weight:600;display:block}
.brand{margin-left:auto;font-family:'Montserrat',Arial,sans-serif;font-size:16px;font-weight:600;color:var(--white)}
</style>
</head>
<body>

<section class="card card--front">
  <div class="front-inner">
    <svg class="hero" viewBox="0 0 672 210" role="img" aria-label="Photo of a client signing papers at a desk with a lawyer, warm window light">
      <defs>
        <linearGradient id="heroTone" x1="0" y1="0" x2="1" y2="0.4">
          <stop offset="0" stop-color="#c8442f"/>
          <stop offset="0.35" stop-color="#f0a040"/>
          <stop offset="0.55" stop-color="#b3202b"/>
          <stop offset="0.85" stop-color="#4a1a22"/>
          <stop offset="1" stop-color="#241a20"/>
        </linearGradient>
      </defs>
      <path d="M0 0H672V210C480 160 240 150 0 190Z" fill="url(#heroTone)"/>
    </svg>
    <div class="hero-title">
      <span class="firm">Bayview Family Law Group</span>
      <span class="tagline">Your Seaport Family Lawyer</span>
    </div>

    <div class="levels">
      <article class="level">
        <span class="num">1</span>
        <h2>Empowered level</h2>
        <p>Absolutely free, no obligation telephone consultation. Free access to simplified court forms. Free book plus free gift with your call. Our free consultation is proudly offered as a service to our community and to you.</p>
      </article>
      <article class="level">
        <span class="num">2</span>
        <h2>Signature level</h2>
        <p>All empowered level benefits plus a rich menu of fixed fee tasks tailored to your needs: Court papers, agreements, mediation, lawyer coaching on a budget.</p>
      </article>
      <article class="level level--featured">
        <span class="num">3</span>
        <h2>Partnership level</h2>
        <p>Our most popular and powerful option. Your goals – our team in partnership counseling and litigating for you: pleadings, motions, mediation, court appearances. Child issues, alimony, assets, debts, gifts – your future.</p>
      </article>
      <article class="level level--last">
        <span class="num">4</span>
        <h2>Traditional law practice</h2>
        <p>A dead model that replaces your goals for the broken bureaucratic and impersonal court driven system.</p>
      </article>
    </div>
  </div>
</section>

<section class="card card--back">
  <div class="back-inner">
    <h1 class="chart-title">FAMILY LAW SERVICE OPTIONS</h1>
    <div class="chart">
      <div class="corner">Service Level</div>
      <div class="col-head">Phone Consult</div>
      <div class="col-head">Court Forms</div>
      <div class="col-head">Fixed Fees</div>
      <div class="col-head">Full Team</div>
      <div class="col-head">Court Help</div>

      <div class="row-head">Empowered Level</div>
      <div>Free</div><div>Free</div><div>Yes</div><div>No</div><div>No</div>

      <div class="row-head">Signature Level</div>
      <div>Free</div><div>Free</div><div>Yes</div><div>Optional</div><div>Fee Per Task</div>

      <div class="row-head row-feature">Partnership Level</div>
      <div class="row-feature">Free</div><div class="row-feature">Free</div><div class="row-feature">Optional</div><div class="row-feature">Yes</div><div class="row-feature">Yes</div>

      <div class="row-head">Traditional Practice Model</div>
      <div>Maybe</div><div>No</div><div>No</div><div>Yes</div><div>Yes</div>
    </div>
    <footer class="chart-footer">
      <p class="address">214 Shore Road<br>Seaport, NJ 08700</p>
      <span class="divider"></span>
      <p class="contact"><strong>732.555.0148</strong>www.bayviewfamilylaw.net</p>
      <div class="brand">Bayview</div>
    </footer>
  </div>
</section>

</body>
</html>
```